Floor Inspections and Consulting

We provide inspections and consulting services on various floor coverings, e.g. carpet, hardwood, etc. We also do expert witness work for attorneys due to floor covering failures. We current have a logo, just need it incorporated into a new design. I have examples of cards I have found on the internet that capture my attention and make a statement. I have included our original business card, which in my opinion is terrible, but it does have our logo on it.

```html
<!DOCTYPE html>
<html lang="en">
<head>
<meta charset="utf-8">
<title>Northfield Floor Inspections – Business Card</title>
<link href="https://fonts.googleapis.com/css2?family=Montserrat:wght@500;700;800&display=swap" rel="stylesheet">
<style>
  :root {
    --canvas: #c9c9c9;
    --shadow: #8c8c8c;
    --card-black: #0b0b0b;
    --red: #e8413a;
    --white: #ffffff;
    --ink: #111111;
  }
  * { box-sizing: border-box; margin: 0; padding: 0; }
  html, body { width: 1200px; height: 1200px; overflow: hidden; }
  body {
    background: var(--canvas);
    font-family: "Montserrat", Arial, sans-serif;
    display: flex; flex-direction: column; align-items: center; justify-content: center;
    gap: 64px;
  }
  .card {
    position: relative;
    width: 860px; height: 494px;
    background: var(--card-black);
    box-shadow: 14px 14px 0 var(--shadow);
    overflow: hidden;
  }
  .card__texture { position: absolute; inset: 0 0 39px 0; background: var(--card-black); }
  .card__band {
    position: absolute; left: 0; right: 0; bottom: 0; height: 39px;
    background: var(--red);
    display: flex; align-items: center; justify-content: center;
    padding-left: 370px;
  }
  .card__web { color: var(--white); font-weight: 700; font-size: 17px; }

  .brand { position: absolute; display: flex; align-items: center; gap: 18px; }
  .brand__dot { width: 96px; height: 96px; border-radius: 50%; background: var(--red); flex: none; }
  .brand__name {
    color: var(--white); font-weight: 800; font-size: 26px; line-height: 1.2;
    text-transform: uppercase; letter-spacing: 0.5px;
  }
  .card--front .brand { left: 34px; top: 150px; width: 320px; }
  .card--back .brand { left: 50%; top: 50%; transform: translate(-50%, -58%); }
  .card--back .brand__dot { width: 130px; height: 130px; }
  .card--back .brand__name { font-size: 34px; }

  .name-bar {
    position: absolute; left: 370px; right: 0; top: 206px; height: 63px;
    background: var(--red);
    display: flex; align-items: center; padding-left: 24px;
  }
  .name-bar__text { color: var(--ink); font-weight: 800; font-size: 40px; letter-spacing: 0.5px; }

  .contact { position: absolute; left: 386px; top: 300px; display: flex; flex-direction: column; gap: 18px; }
  .contact__row { display: flex; align-items: center; gap: 14px; color: var(--white); font-size: 18px; font-weight: 500; }
  .contact__icon { width: 38px; height: 38px; flex: none; }
</style>
</head>
<body>

  <section class="card card--front">
    <div class="card__texture" role="img" aria-label="Dark background with a scattered pattern of grey squares"></div>
    <div class="brand">
      <span class="brand__dot"></span>
      <span class="brand__name">Northfield Floor Inspections</span>
    </div>
    <div class="name-bar"><span class="name-bar__text">DANA HOLLOWAY</span></div>
    <div class="contact">
      <div class="contact__row">
        <svg class="contact__icon" viewBox="0 0 38 38" aria-hidden="true">
          <circle cx="19" cy="19" r="16" fill="none" stroke="var(--red)" stroke-width="3"/>
          <path d="M13 11 l4 -1 2 5 -2.5 2 a11 11 0 0 0 4.5 4.5 l2 -2.5 5 2 -1 4 c-8 1 -15 -6 -14 -14z" fill="var(--red)"/>
        </svg>
        <span>555-014-2870</span>
      </div>
      <div class="contact__row">
        <svg class="contact__icon" viewBox="0 0 38 38" aria-hidden="true">
          <circle cx="19" cy="19" r="16" fill="none" stroke="var(--red)" stroke-width="3"/>
          <rect x="10" y="13" width="18" height="12" fill="var(--red)"/>
          <path d="M10 13 l9 7 9 -7" fill="none" stroke="var(--card-black)" stroke-width="1.6"/>
        </svg>
        <span>dana@northfieldfloors.com</span>
      </div>
    </div>
    <div class="card__band"><span class="card__web">northfieldfloors.com</span></div>
  </section>

  <section class="card card--back">
    <div class="card__texture" role="img" aria-label="Dark background with a scattered pattern of grey squares"></div>
    <div class="brand">
      <span class="brand__dot"></span>
      <span class="brand__name">Northfield<br>Floor Inspections</span>
    </div>
    <div class="card__band" style="padding-left:0"></div>
  </section>

</body>
</html>
```